Beef 100 % Cooked Ready to Eat in a Metal Can

Design a label for a Beef Product 100 % Pure ,Cooked and ready to eat , Be sold in Africa . The label to be in English and French , Or English and Portuguese . Need either a photo or a drawing showing a Bull or Cow .

BRAND Name of the product is " 100% BEEF
Plus + Picture of a Bull or Cow and after to expand Range to include 100 % Mutton , The label should be easy to reproduce and Art work in BALCK AND WHITE for point of sale POSTERS for Advertising . T Shirts ect
Updates

Check out the updated Brief ,and Maybe I will in crease the Budget !

Target Market(s)

African People , Children , illiterate ,Some of the target People who Can read and some can't , From Age 16 - 40 males and female

Image /drawing /or Photo of Bull Or Cow must be Prominent ,

The word 100 % BEEF . Most People can Understand even the ones that cat read

Background color should be stand out form Competitors

Industry/Entity Type

Advertising

Font styles to use
Sans Serif

Colors

Designer to choose colors to be used in the design.

Requirements
Must have

• Recognizable ,easy to remember , Symbols , Image +100%+ Beef = Good Label

Bright Colour ,
Nice to have
• Positive color

Simple Not too Much Copy .

Tin Will Have Ingredients in Small and Bar code in Small .
Should not have
• Modern look .as for Traditional ,Market ,

```html
<!DOCTYPE html>
<html lang="en">
<head>
<meta charset="UTF-8">
<title>100% Beef – Can Label</title>
<link rel="stylesheet" href="https://fonts.googleapis.com/css2?family=Tinos:wght@400;700&display=swap">
<style>
  :root {
    --stage-top: #f4f4f4;
    --stage-bottom: #dedede;
    --label-red: #dc0f2b;
    --label-red-deep: #a9081f;
    --gold: #e3ad16;
    --gold-light: #f7d84a;
    --white: #ffffff;
    --title-yellow: #f7d417;
    --ink: #1a1a1a;
    --art-light: #f8f4f3;
    --art-shade: #e6dcda;
    --cow-brown: #c8743c;
    --cow-cream: #f1dccb;
  }
  html, body {
    margin: 0;
    padding: 0;
    overflow: hidden;
  }
  .canvas {
    position: relative;
    width: 1200px;
    height: 664px;
    overflow: hidden;
    background: linear-gradient(var(--stage-top), var(--stage-bottom));
  }
  .label {
    position: absolute;
    left: 300px;
    top: 122px;
    width: 600px;
    height: 456px;
    background: var(--label-red);
    overflow: hidden;
  }
  .label__rule {
    position: absolute;
    left: 0;
    width: 100%;
    height: 7px;
    background: linear-gradient(var(--gold-light), var(--gold));
  }
  .label__rule--top { top: 26px; }
  .label__rule--bottom { top: 420px; }
  .label__band {
    position: absolute;
    left: 0;
    top: 286px;
    width: 100%;
    height: 90px;
    background: linear-gradient(var(--gold-light), var(--gold) 60%, var(--gold-light));
  }
  .emblem {
    position: absolute;
    left: 120px;
    top: 53px;
    width: 360px;
    height: 360px;
    box-sizing: border-box;
    border-radius: 50%;
    background: var(--white);
  }
  .emblem__ring {
    position: absolute;
    inset: 8px;
    border-radius: 50%;
    border: 3px solid var(--label-red);
  }
  .emblem__art {
    position: absolute;
    inset: 15px;
    border-radius: 50%;
    background:
      radial-gradient(ellipse 38% 26% at 50% 46%, var(--cow-brown) 0%, rgba(200,116,60,0.55) 55%, rgba(241,220,203,0) 100%),
      radial-gradient(ellipse 55% 38% at 50% 48%, var(--cow-cream) 0%, rgba(241,220,203,0) 100%),
      radial-gradient(circle at 50% 40%, var(--art-light) 0%, var(--art-light) 50%, var(--art-shade) 100%);
  }
  .ribbon {
    position: absolute;
    left: 0;
    top: 0;
    width: 600px;
    height: 456px;
  }
  .brand-title {
    position: absolute;
    left: 165px;
    top: 274px;
    width: 270px;
    margin: 0;
    text-align: center;
    font-family: "Tinos", "Times New Roman", serif;
    font-weight: 700;
    font-size: 40px;
    line-height: 100px;
    color: var(--title-yellow);
  }
  .range-note {
    position: absolute;
    left: 220px;
    top: 379px;
    width: 160px;
    margin: 0;
    text-align: center;
    font-family: "Tinos", "Times New Roman", serif;
    font-size: 13px;
    line-height: 16px;
    color: var(--ink);
  }
</style>
</head>
<body>
<div class="canvas">
  <div class="label">
    <div class="label__rule label__rule--top"></div>
    <div class="label__band"></div>
    <div class="label__rule label__rule--bottom"></div>

    <div class="emblem">
      <div class="emblem__ring"></div>
      <div class="emblem__art" role="img" aria-label="Illustration of a brown and white cow standing, facing left"></div>
    </div>

    <svg class="ribbon" viewBox="0 0 600 456" aria-hidden="true">
      <polygon points="93,283 172,283 172,386 93,386 133,334" fill="var(--label-red)" stroke="var(--white)" stroke-width="3" stroke-linejoin="round"/>
      <polygon points="507,283 428,283 428,386 507,386 467,334" fill="var(--label-red)" stroke="var(--white)" stroke-width="3" stroke-linejoin="round"/>
      <polygon points="165,372 172,386 172,372" fill="var(--label-red-deep)"/>
      <polygon points="435,372 428,386 428,372" fill="var(--label-red-deep)"/>
      <rect x="165" y="274" width="270" height="100" rx="8" fill="var(--label-red)" stroke="var(--white)" stroke-width="3"/>
    </svg>

    <p class="brand-title">100% BEEF</p>
    <p class="range-note">100% Mutton</p>
  </div>
</div>
</body>
</html>
```